Business Card Design and a letter head logo

50/50 share milker dairy farmer of 400 cows with a silage and haymaking sideline business
15 years farming currently looking for new opportunities within the dairy farming sector. trying to put together a portfolio to get another 50/50 share milking job aswell

Industry/Entity Type

Farming

Contact Information for Business Card

Birch Farming LTD
Corwin & Felicity Hartley
382 Kelvale Ridge Highway
RD1 Tawhiro 0184
Whangarei
hartley.corwin@lumenmail.co.nz
0273948261
(09) 4715293

```html
<!DOCTYPE html>
<html lang="en">
<head>
<meta charset="utf-8">
<title>Birch Farming LTD – Business Card</title>
<link rel="stylesheet" href="https://fonts.googleapis.com/css2?family=Noto+Sans:wght@400&family=Open+Sans:wght@400&display=swap">
<style>
  :root {
    --backdrop: #3b3b3b;
    --card: #000000;
    --green: #2e9a55;
    --red: #e23232;
    --white: #ffffff;
  }
  * { box-sizing: border-box; margin: 0; padding: 0; }
  html, body { width: 1200px; height: 800px; overflow: hidden; background: var(--backdrop); }
  .canvas {
    width: 1200px; height: 800px;
    display: flex; align-items: center; justify-content: center;
  }
  .card {
    position: relative;
    width: 1000px; height: 600px;
    background: var(--card);
    border-radius: 34px;
    display: grid;
    grid-template-columns: 460px 1px 1fr;
    box-shadow: 0 10px 30px rgba(0,0,0,0.45);
  }
  .brand {
    display: flex; align-items: center; justify-content: center; gap: 14px;
    padding-top: 20px;
  }
  .brand-mark {
    width: 22px; height: 22px; background: var(--green);
  }
  .brand-name {
    font-family: "Open Sans", sans-serif;
    font-weight: 400;
    font-size: 38px;
    color: var(--green);
    letter-spacing: 0.3px;
  }
  .divider {
    align-self: center;
    height: 360px;
    background: linear-gradient(to bottom, rgba(46,154,85,0), var(--green) 25%, var(--green) 75%, rgba(46,154,85,0));
  }
  .contact {
    font-family: "Noto Sans", sans-serif;
    color: var(--white);
    padding: 118px 48px 0 40px;
    display: flex; flex-direction: column; align-items: flex-end;
  }
  .holders {
    color: var(--green);
    font-size: 25px;
    margin-right: 58px;
    margin-bottom: 62px;
    letter-spacing: 0.4px;
  }
  .contact-row {
    display: flex; align-items: flex-start; gap: 16px;
    font-size: 23px; letter-spacing: 0.6px;
    margin-bottom: 22px;
    text-align: right;
    line-height: 1.3;
  }
  .contact-row.phone { font-size: 25px; letter-spacing: 1.5px; }
  .icon { width: 42px; height: 40px; flex: none; }
  .address { margin-top: 6px; }
</style>
</head>
<body>
<main class="canvas">
  <section class="card">
    <div class="brand">
      <span class="brand-mark"></span>
      <span class="brand-name">Birch Farming LTD</span>
    </div>

    <div class="divider"></div>

    <div class="contact">
      <p class="holders">Corwin &amp; Felicity Hartley</p>

      <div class="contact-row phone">
        <span>0273948261</span>
        <svg class="icon" viewBox="0 0 42 40" aria-hidden="true">
          <polygon points="21,2 39,13 35,35 7,35 3,13" fill="var(--red)"/>
          <path d="M15 12 l4 -1 l2 5 l-3 2 q2 4 6 6 l2 -3 l5 2 l-1 4 q-10 1 -15 -15z" fill="var(--white)"/>
        </svg>
      </div>

      <div class="contact-row">
        <span>hartley.corwin@lumenmail.co.nz</span>
        <svg class="icon" viewBox="0 0 42 40" aria-hidden="true">
          <polygon points="21,2 39,13 35,35 7,35 3,13" fill="var(--red)"/>
          <rect x="11" y="13" width="20" height="13" fill="none" stroke="var(--white)" stroke-width="2"/>
          <polyline points="11,13 21,21 31,13" fill="none" stroke="var(--white)" stroke-width="2"/>
        </svg>
      </div>

      <div class="contact-row address">
        <span>382 Kelvale Ridge Highway<br>RD1 Tawhiro 0184<br>Whangarei</span>
        <svg class="icon" viewBox="0 0 42 40" aria-hidden="true">
          <polygon points="21,2 39,13 35,35 7,35 3,13" fill="var(--red)"/>
          <path d="M21 29 l-6 -9 a7 7 0 1 1 12 0z" fill="var(--white)"/>
          <circle cx="21" cy="16" r="2.6" fill="var(--red)"/>
        </svg>
      </div>
    </div>
  </section>
</main>
</body>
</html>
```